Soap/cosmetic labels

Need labels that incorporate my brand , to fit onto rectangular and round labels readable down to two inches. Key ideas are luxury, nourishing, handmade, palm oil/paraben free, cruelty free, savon artisanal. One line will be called The Gentle Cake by The Meadow Wren with key words: fragrance free, all natural colorants. The other line is luxury oils, fragrance, indulgent and just The Meadow Wren

Target Market(s)

Women mostly

Industry/Entity Type

cosmetics/soap

Colors
0094D4
00A9DD
6FCCEA
C7EBF8
E9F6FB

Requirements
Must have
• place for me to change fragrance and cosmetic type; gold goes on black labels; blue on white labels
Nice to have
• fit the brand

```html
<!DOCTYPE html>
<html lang="en">
<head>
<meta charset="utf-8">
<title>The Gentle Cake – Soap Label</title>
<link rel="stylesheet" href="https://fonts.googleapis.com/css2?family=Cinzel:wght@400;600;700&family=Pinyon+Script&display=swap">
<style>
  :root {
    --label-blue: #00A9DD;
    --label-blue-deep: #0094D4;
    --label-rim: #000000;
    --label-paper: #FFFFFF;
  }
  html, body {
    margin: 0;
    padding: 0;
    width: 1200px;
    height: 1200px;
    overflow: hidden;
    background: var(--label-paper);
  }
  .label {
    display: block;
    width: 1200px;
    height: 1200px;
  }
  .label__rim { fill: var(--label-paper); stroke: var(--label-rim); stroke-width: 6; }
  .label__inner-ring { fill: none; stroke: var(--label-blue); stroke-width: 3; }
  .label__emblem { fill: var(--label-blue); }
  .label__arc-text {
    font-family: "Cinzel", serif;
    font-weight: 400;
    font-size: 38px;
    letter-spacing: 6px;
    fill: var(--label-blue);
  }
  .label__tagline {
    font-family: "Pinyon Script", cursive;
    font-size: 54px;
    fill: var(--label-blue);
  }
  .label__product-name {
    font-family: "Cinzel", serif;
    font-weight: 700;
    font-size: 76px;
    fill: var(--label-blue);
  }
  .label__keywords {
    font-family: "Pinyon Script", cursive;
    font-size: 36px;
    fill: var(--label-blue);
  }
  .label__brand {
    font-family: "Cinzel", serif;
    font-weight: 600;
    font-size: 56px;
    fill: var(--label-blue);
  }
</style>
</head>
<body>
<svg class="label" viewBox="0 0 1200 1200" xmlns="http://www.w3.org/2000/svg">
  <defs>
    <path id="arc-top" d="M 170 600 A 430 430 0 0 1 1030 600"/>
    <path id="arc-bottom" d="M 1030 600 A 430 430 0 0 1 170 600"/>
  </defs>

  <circle class="label__rim" cx="600" cy="600" r="510"/>
  <circle class="label__inner-ring" cx="600" cy="600" r="480"/>

  <text class="label__arc-text">
    <textPath href="#arc-top" startOffset="50%" text-anchor="middle">SAVON ARTISANAL • HANDMADE</textPath>
  </text>
  <text class="label__arc-text">
    <textPath href="#arc-bottom" startOffset="50%" text-anchor="middle">PALM OIL &amp; PARABEN FREE • CRUELTY FREE</textPath>
  </text>

  <circle class="label__emblem" cx="600" cy="325" r="76" role="img" aria-label="Brand emblem area"/>

  <text class="label__tagline" x="600" y="494" text-anchor="middle">Nourishing</text>
  <text class="label__product-name" x="600" y="630" text-anchor="middle" textLength="900" lengthAdjust="spacingAndGlyphs">THE GENTLE CAKE</text>
  <text class="label__keywords" x="600" y="703" text-anchor="middle">fragrance free, all natural colorants</text>

  <text class="label__brand" x="600" y="875" text-anchor="middle">The Meadow Wren</text>
</svg>
</body>
</html>
```